Exciting New Reseller Brand requires Website to WOW New clients to register.

We are a NEW online business called Trade Your Goods.

The Website is a simple concept, it looks to put Merchants (businesses that want their products resold) in touch with Resellers (people or businesses that want to resell that product).

The website acts as an online market place which looks to get Merchants to sign-up and pay to list their company and product as well as getting Resellers to sign-up to view potential Merchants they can get in touch with in the right industry or area to resell their products for (see attached slide-pack to explain packages)

Any type of Industry or Business can register themselves to get listed on Trade Your Goods to see either get their product/service resold or to look for products / services to reseller.

Trade Your Goods does not take any other monetary part in the business relationships other than to obtain money for the monthly website subscription.

We want a very simple website, so this project is for several pages:

Page 1) A really vibrant, exciting, image based homepage to get people to sign-up / register (see sites that we like in the project brief). Needs to be very clear that there are 2 customers and to sign up to join, build and earn!

Page 2) A page that describes the benefits and packages for Resellers.

Page 3) A page that describes the benefits and packages for Merchants.

Page 4) The Payment process pages, taking the customer through sign-up

Page 5) The Business Listings page, so when people search for a Merchant how this will be displayed.

We would really like an image based site and preferably parallax. We want it bright vibrant and to look like a social media site.

All necessary files / logos enclosed.

We would love to continue to work with the winning designer moving forward.

Many thanks and Good Luck.

Regards

Martin & Owen

Target Market(s)

Merchants, Suppliers, Vendors, Manufacturers, Distributors, Wholesalers, Affiliate programs, Franchisees, Reselers

Industry/Entity Type

Business

Number of Pages Required

5+ page

Requirements
Must have
• We love the following websites:
• 1) Like the top section, i.e. parallax image based: www.brightfoxstudio.co.uk
• 2) Like the way the screen is split in 2, could be used to describe the 2 different customers we are after Merchants / Resellers: www.cloudtrunk.example/guide
• 3) Like the bright colours / full screen video split into 2 below top banner and the generally how simple the site is: www.harbourlinden.com.au
• 4) Love all of this site, simple, bold, Love the colours, the clear message and the infographics: http://www.velomiro.example/swiftride/quicker

```html
<!DOCTYPE html>
<html lang="en">
<head>
<meta charset="utf-8">
<title>Trade Your Goods</title>
<link href="https://fonts.googleapis.com/css2?family=Raleway:wght@300;400;500;600&family=Montserrat:wght@600;700&family=Open+Sans:wght@400;600;700&display=swap" rel="stylesheet">
<style>
:root{
  --blue:#1a8ad4;
  --blue-deep:#0f6fb3;
  --green:#8cc63f;
  --green-deep:#7ab531;
  --dark:#1e2126;
  --ink:#333;
  --muted:#666;
  --light:#f0f0f0;
  --grey-hex:#8a8a8a;
  --white:#fff;
}
*{box-sizing:border-box;margin:0;padding:0}
html,body{width:1200px;height:4500px;overflow:hidden}
body{font-family:"Open Sans",Arial,sans-serif;color:var(--ink);background:var(--white)}
section{position:relative;width:1200px;overflow:hidden}
.abs{position:absolute}

/* hero */
.hero{height:655px;background:linear-gradient(160deg,#3c4552 0%,#262b33 45%,#151719 100%)}
.hero-photo{position:absolute;inset:0;background:radial-gradient(ellipse at 75% 55%,rgba(120,130,140,.35),transparent 60%),radial-gradient(ellipse at 25% 30%,rgba(90,110,140,.3),transparent 55%)}
.brand{position:absolute;left:100px;top:28px;display:flex;align-items:center;gap:12px;color:var(--white);font-family:"Raleway",sans-serif;font-weight:600;font-size:30px}
.brand-dot{width:52px;height:52px;border-radius:50%;background:var(--white)}
.nav{position:absolute;right:100px;top:58px;display:flex;gap:38px;font-family:"Open Sans",sans-serif;font-size:15px;color:var(--white)}
.hero-title{position:absolute;top:292px;width:100%;text-align:center;color:var(--white);font-family:"Raleway",sans-serif;font-weight:400;font-size:36px;letter-spacing:1px}
.hero-sub{position:absolute;top:345px;width:100%;text-align:center;color:var(--white);font-family:"Raleway",sans-serif;font-size:24px;letter-spacing:1px}

/* split */
.split{height:300px;display:flex}
.split-half{width:600px;height:300px;text-align:center;color:var(--white);padding-top:50px}
.split-half.merchants{background:var(--blue)}
.split-half.resellers{background:var(--green)}
.split-title{font-family:"Montserrat",sans-serif;font-weight:700;font-size:60px;letter-spacing:1px;line-height:1}
.split-sub{font-family:"Open Sans",sans-serif;font-weight:600;font-size:20px;margin-top:24px}
.btn-outline{display:inline-block;margin-top:30px;border:2px solid var(--white);padding:14px 30px;font-weight:700;font-size:16px}

/* why */
.why{height:400px;background:var(--white)}
.why-title{left:132px;top:28px;font-family:"Raleway",sans-serif;font-size:44px;color:var(--green);letter-spacing:1px}
.why-sub{left:132px;top:90px;font-family:"Raleway",sans-serif;font-size:33px;color:#777;line-height:1.1}
.why-big{left:132px;top:128px;font-family:"Raleway",sans-serif;font-size:62px;color:#666}
.arrow-list{list-style:none;font-family:"Raleway",sans-serif;font-size:19px;color:#777;line-height:29px}
.arrow-list li::before{content:"→ ";color:var(--green)}
.why-list{left:140px;top:228px}
.why-art{left:665px;top:25px;width:340px;height:340px;border-radius:12px;background:radial-gradient(circle at 50% 60%,#c7d9ee 0%,#e9eef4 55%,#fff 80%)}

/* company */
.company{height:370px;background:var(--light)}
.company-art{left:190px;top:40px;width:300px;height:290px;border-radius:10px;background:linear-gradient(145deg,#3a2b6e,#1b5fa8 55%,#d9dde2)}
.company-title{left:648px;top:22px;font-family:"Raleway",sans-serif;font-size:42px;color:var(--blue)}
.company-text{left:663px;top:82px;width:460px;font-size:14px;color:var(--muted);line-height:20px}
.company-list{left:663px;top:140px;font-size:18px;line-height:29px}
.company-list li::before{color:var(--blue)}

/* blog */
.blog{height:705px;background:linear-gradient(150deg,#2a2d33,#4b4f56 50%,#1d1f23)}
.section-title{position:absolute;width:100%;text-align:center;font-family:"Raleway",sans-serif;font-size:36px}
.section-lead{position:absolute;left:180px;width:840px;text-align:center;font-weight:700;font-size:14px;line-height:24px}
.blog .section-title,.blog .section-lead{color:var(--white)}
.card{position:absolute;width:270px;background:var(--white);box-shadow:0 4px 12px rgba(0,0,0,.35);padding-bottom:14px}
.card-img{height:195px;background:linear-gradient(160deg,#d8dde4,#8e9aa8)}
.card-body{padding:12px 12px 0}
.card-title{font-weight:700;font-size:15px;line-height:21px;color:#222}
.card-text{font-size:13px;line-height:19px;color:#555;margin-top:6px}
.card-meta{display:flex;align-items:center;gap:8px;margin-top:10px;border-top:1px solid #e5e5e5;padding-top:8px;font-size:11px;color:#777;line-height:14px}
.card-avatar{width:26px;height:26px;border-radius:50%;background:#b9a89a}

/* how */
.how{height:485px;background:#fafafa}
.how .section-title{color:#444}
.how .section-lead{color:#555}
.hex-label{position:absolute;width:120px;text-align:center;font-size:14px;color:#444}

/* benefits */
.benefits{height:470px;background:linear-gradient(150deg,#2b2e34,#474b52 55%,#202226)}
.benefits .section-title,.benefits .section-lead{color:var(--white)}
.benefit{position:absolute;top:155px;width:378px}
.benefit-head{height:50px;line-height:50px;text-align:center;font-family:"Raleway",sans-serif;font-size:32px;color:var(--white)}
.benefit-head.merchants{background:var(--blue)}
.benefit-head.resellers{background:var(--green)}
.benefit-box{background:var(--white);height:200px;margin:0 10px;padding:16px 22px}
.tick-list{list-style:none;font-size:16px;line-height:30px}
.tick-list li{display:flex;align-items:center;gap:14px;color:var(--blue-deep)}
.resellers-list li{color:#4a7cc2}

/* clients */
.clients{height:520px;background:var(--white)}
.clients .section-title{color:#555}
.clients .section-lead{color:#666;font-weight:600}
.client-photo{left:540px;top:160px;width:120px;height:120px;border-radius:50%;border:5px solid #e8e8e8;background:linear-gradient(150deg,#d6c9bc,#8a7d72)}
.quote{left:120px;top:305px;width:960px;text-align:center;font-size:14px;line-height:24px;color:#555}
.client-name{top:420px;width:100%;text-align:center;font-weight:700;font-size:14px;letter-spacing:1px;color:#333}
.client-company{top:448px;width:100%;text-align:center;font-weight:700;font-size:14px;color:#333}
.dots{left:510px;top:485px;display:flex;gap:10px}
.dots span{width:40px;height:5px;background:#ddd}
.dots span.on{background:var(--blue)}

/* quotes */
.quotes{height:475px;background:linear-gradient(180deg,var(--blue),var(--blue-deep))}
.quotes .section-title,.quotes .section-lead{color:var(--white)}
.field{position:absolute;left:212px;width:800px;height:42px;border:1px solid rgba(255,255,255,.7);color:var(--white);font-style:italic;font-size:14px;padding:11px 12px}
.submit{left:522px;top:384px;width:156px;height:50px;background:var(--green);color:var(--white);text-align:center;line-height:50px;font-size:17px}

/* footer */
.footer{height:120px;background:var(--white)}
.social{left:490px;top:24px;display:flex;gap:8px}
.social span{width:38px;height:38px;border-radius:50%;background:#222}
.copyright{top:80px;width:100%;text-align:center;font-size:13px;color:#444}
</style>
</head>
<body>

<section class="hero">
  <div class="hero-photo" role="img" aria-label="Photo of a person working on a laptop at a desk"></div>
  <div class="brand"><span class="brand-dot"></span>Trade Your Goods</div>
  <nav class="nav"><span>Home</span><span>About Us</span><span>Services</span><span>Our Work</span><span>Products</span><span>Contact</span></nav>
  <h1 class="hero-title">BUILDING YOUR OWN VIRTUAL SALES TEAM</h1>
  <p class="hero-sub">JOIN, BUILD, EARN</p>
</section>

<section class="split">
  <div class="split-half merchants">
    <h2 class="split-title">MERCHANTS</h2>
    <p class="split-sub">Register to build your virtual sales team</p>
    <span class="btn-outline">Build Sales Team</span>
  </div>
  <div class="split-half resellers">
    <h2 class="split-title">RESELLERS</h2>
    <p class="split-sub">Register to start earning money</p>
    <span class="btn-outline">Earn Money now</span>
  </div>
</section>

<section class="why">
  <h2 class="abs why-title">WHY PICK RESELLING</h2>
  <p class="abs why-sub">Bringing reseller opportunities</p>
  <p class="abs why-big">to the masses..</p>
  <ul class="abs arrow-list why-list">
    <li>Personal requirement for a reseller base.</li>
    <li>Experienced reseller models that work.</li>
    <li>Building an effective virtual sales team.</li>
    <li>Helping SME's earn money for old rope.</li>
    <li>Easy to generate revenue for a minimal cost.</li>
  </ul>
  <div class="abs why-art" role="img" aria-label="Illustration of business figures joining puzzle pieces"></div>
</section>

<section class="company">
  <div class="abs company-art" role="img" aria-label="Desktop computer showing the website"></div>
  <h2 class="abs company-title">Company Information</h2>
  <p class="abs company-text">Lorem Ipsum is simply dummy text of the printing and typesetting industry. Lorem Ipsum has been the industry's</p>
  <ul class="abs arrow-list company-list">
    <li>Portal for Resellers and Merchants.</li>
    <li>Merchants can promote their products.</li>
    <li>Merchants can build a virtual sales team.</li>
    <li>Resellers can expand product portfolio.</li>
    <li>Resellers can generate revenue.</li>
    <li>Industry news and opportunities.</li>
  </ul>
</section>

<section class="blog" role="region" aria-label="Blog posts over a photo of a laptop desk">
  <h2 class="section-title" style="top:28px">Blog Post</h2>
  <p class="section-lead" style="top:82px">Lorem Ipsum is simply dummy text of the printing and typesetting industry. Lorem Ipsum has been the industry's standard dummy text ever since the 1500s, when an unknown printer took</p>
  <article class="card" style="left:140px;top:260px">
    <div class="card-img" role="img" aria-label="Photo of team hands stacked together"></div>
    <div class="card-body">
      <h3 class="card-title">How I Create Graphics for My Blog &amp; Business</h3>
      <p class="card-text">In frequently asked how I create graphics for my blog posts, design printables and planners for...</p>
      <div class="card-meta"><span class="card-avatar"></span><span>Lena Hart<br>Blogging tips</span></div>
    </div>
  </article>
  <article class="card" style="left:483px;top:185px">
    <div class="card-img" role="img" aria-label="Photo of a business team standing together"></div>
    <div class="card-body">
      <h3 class="card-title">How I Create Graphics for My Blog &amp; Business</h3>
      <p class="card-text">In frequently asked how I create graphics for my blog posts, design printables and planners for...</p>
      <div class="card-meta"><span class="card-avatar"></span><span>Lena Hart<br>Blogging tips</span></div>
    </div>
  </article>
  <article class="card" style="left:822px;top:260px">
    <div class="card-img" role="img" aria-label="Photo of colleagues in a meeting"></div>
    <div class="card-body">
      <h3 class="card-title">How I Create Graphics for My Blog &amp; Business</h3>
      <p class="card-text">In frequently asked how I create graphics for my blog posts, design printables and planners for...</p>
      <div class="card-meta"><span class="card-avatar"></span><span>Lena Hart<br>Blogging tips</span></div>
    </div>
  </article>
</section>

<section class="how">
  <h2 class="section-title" style="top:40px">How it Works</h2>
  <p class="section-lead" style="top:98px">Lorem Ipsum is simply dummy text of the printing and typesetting industry. Lorem Ipsum has been the industry's standard dummy text ever since the 1500s, when an unknown printer took</p>
  <svg class="abs" style="left:0;top:180px" width="1200" height="240" viewBox="0 0 1200 240">
    <g fill="none" stroke="#ccc" stroke-width="2">
      <path d="M170 70 Q210 50 250 70"/><path d="M300 70 Q340 50 380 70"/>
      <path d="M810 70 Q850 50 890 70"/><path d="M940 70 Q980 50 1020 70"/>
    </g>
    <g fill="var(--blue)">
      <polygon points="150,72 200,72 225,115 200,158 150,158 125,115" transform="translate(-25,0)"/>
      <polygon points="280,72 330,72 355,115 330,158 280,158 255,115" transform="translate(-20,0)"/>
      <polygon points="410,72 460,72 485,115 460,158 410,158 385,115" transform="translate(-15,0)"/>
    </g>
    <polygon points="555,40 645,40 690,117 645,194 555,194 510,117" fill="var(--grey-hex)"/>
    <text x="600" y="113" text-anchor="middle" fill="#fff" font-family="Raleway,sans-serif" font-size="24">PROMOTE</text>
    <text x="600" y="141" text-anchor="middle" fill="#fff" font-family="Raleway,sans-serif" font-size="24">AND EARN</text>
    <g fill="var(--green)">
      <polygon points="765,72 815,72 840,115 815,158 765,158 740,115"/>
      <polygon points="895,72 945,72 970,115 945,158 895,158 870,115"/>
      <polygon points="1025,72 1075,72 1100,115 1075,158 1025,158 1000,115"/>
    </g>
    <g fill="none" stroke="#fff" stroke-width="3">
      <circle cx="150" cy="108" r="9"/><path d="M132 132 Q150 112 168 132"/>
      <path d="M262 118 l12 10 l20 -22"/>
      <rect x="381" y="98" width="28" height="34" rx="2"/><path d="M387 110h16M387 120h16"/>
      <circle cx="787" cy="112" r="11"/><path d="M795 120l10 10"/>
      <circle cx="915" cy="108" r="9"/><path d="M900 132 Q915 114 930 132"/><path d="M932 104v12M926 110h12"/>
      <circle cx="1044" cy="106" r="7"/><circle cx="1058" cy="106" r="7"/><path d="M1032 132 Q1050 112 1068 132"/>
    </g>
  </svg>
  <span class="hex-label" style="left:90px;top:350px">Merchants</span>
  <span class="hex-label" style="left:220px;top:350px">Payment</span>
  <span class="hex-label" style="left:350px;top:350px">Listing</span>
  <span class="hex-label" style="left:730px;top:350px">Search</span>
  <span class="hex-label" style="left:860px;top:350px">Register</span>
  <span class="hex-label" style="left:990px;top:350px">Resellers</span>
</section>

<section class="benefits" role="region" aria-label="Benefits over a photo of a workspace">
  <h2 class="section-title" style="top:22px">Benefits For Everyone</h2>
  <p class="section-lead" style="top:72px">Lorem Ipsum is simply dummy text of the printing and typesetting industry. Lorem Ipsum has been the industry's standard dummy text ever since the 1500s, when an unknown printer took</p>
  <div class="benefit" style="left:148px">
    <div class="benefit-head merchants">Merchants</div>
    <div class="benefit-box">
      <ul class="tick-list">
        <li><svg width="16" height="14" viewBox="0 0 16 14"><path d="M1 7l5 5L15 1" fill="none" stroke="var(--blue)" stroke-width="3"/></svg>Additional Source of Sales</li>
        <li><svg width="16" height="14" viewBox="0 0 16 14"><path d="M1 7l5 5L15 1" fill="none" stroke="var(--blue)" stroke-width="3"/></svg>Incremental Growth</li>
        <li><svg width="16" height="14" viewBox="0 0 16 14"><path d="M1 7l5 5L15 1" fill="none" stroke="var(--blue)" stroke-width="3"/></svg>Viral Brand Recognition</li>
        <li><svg width="16" height="14" viewBox="0 0 16 14"><path d="M1 7l5 5L15 1" fill="none" stroke="var(--blue)" stroke-width="3"/></svg>Virtual Sales Team</li>
        <li><svg width="16" height="14" viewBox="0 0 16 14"><path d="M1 7l5 5L15 1" fill="none" stroke="var(--blue)" stroke-width="3"/></svg>No Overheads</li>
      </ul>
    </div>
  </div>
  <div class="benefit" style="left:664px">
    <div class="benefit-head resellers">Resellers</div>
    <div class="benefit-box">
      <ul class="tick-list resellers-list">
        <li><svg width="16" height="14" viewBox="0 0 16 14"><path d="M1 7l5 5L15 1" fill="none" stroke="var(--blue)" stroke-width="3"/></svg>Additional Stream of Income</li>
        <li><svg width="16" height="14" viewBox="0 0 16 14"><path d="M1 7l5 5L15 1" fill="none" stroke="var(--blue)" stroke-width="3"/></svg>Infrastructure in Place</li>
        <li><svg width="16" height="14" viewBox="0 0 16 14"><path d="M1 7l5 5L15 1" fill="none" stroke="var(--blue)" stroke-width="3"/></svg>No Additional Cost</li>
        <li><svg width="16" height="14" viewBox="0 0 16 14"><path d="M1 7l5 5L15 1" fill="none" stroke="var(--blue)" stroke-width="3"/></svg>Expand Product Suite</li>
        <li><svg width="16" height="14" viewBox="0 0 16 14"><path d="M1 7l5 5L15 1" fill="none" stroke="var(--blue)" stroke-width="3"/></svg>Reach New Target Markets</li>
      </ul>
    </div>
  </div>
</section>

<section class="clients">
  <h2 class="section-title" style="top:30px">Our Clientes</h2>
  <p class="section-lead" style="top:90px">Lorem Ipsum is simply dummy text of the printing and typesetting industry. Lorem Ipsum has been the industry's standard dummy text ever since the 1500s, when an unknown printer took</p>
  <div class="abs client-photo" role="img" aria-label="Client portrait"></div>
  <p class="abs quote">A wonderful serenity has taken possession of my entire soul, like these sweet mornings of spring which I enjoy with my whole heartle heart. I am alone, and feel the charm of existence in this spot, which was created for the I am alone, and feel the charm of existence in this spot, which was created for the bliss of souls like mine. I am so happy.</p>
  <p class="abs client-name">SAM RIVERS</p>
  <p class="abs client-company">Brightline Works</p>
  <div class="abs dots"><span class="on"></span><span></span><span></span></div>
</section>

<section class="quotes">
  <h2 class="section-title" style="top:24px">Free Quotes</h2>
  <p class="section-lead" style="top:74px">Lorem Ipsum is simply dummy text of the printing and typesetting industry. Lorem Ipsum has been the industry's standard dummy text ever since the 1500s, when an unknown printer took</p>
  <div class="field" style="top:145px">Enter Name</div>
  <div class="field" style="top:205px">Enter Email</div>
  <div class="field" style="top:265px;height:110px"></div>
  <div class="abs submit">Submit Now</div>
</section>

<footer class="footer" style="position:relative;height:120px">
  <div class="abs social"><span></span><span></span><span></span><span></span><span></span></div>
  <p class="abs copyright">© 2016 Tradeyourgoods.example . All Rights Reserved</p>
</footer>

</body>
</html>
```